" Minha empresa basicamente funciona da seguinte forma, visito os clientes, pego todas as ideias (Briefing), levo para a empresa, elaboramos o melhor projeto possivel para aquele cliente, apresentamos o projeto, o cliente aprovando, começamos a fabricação. E estamos sempre envolvidos em eventos para trazer tecnologia para nossos clientes. "

```html
<!DOCTYPE html>
<html lang="pt-BR">
<head>
<meta charset="UTF-8">
<title>Veranti Móveis Planejados — Papel Timbrado</title>
<link href="https://fonts.googleapis.com/css2?family=Montserrat:wght@300;400;500&display=swap" rel="stylesheet">
<style>
  :root {
    --backdrop: #e4e4e4;
    --paper: #ffffff;
    --taupe: #a88f74;
    --sand: #cbb8a0;
    --ink-grey: #5f5f5f;
    --faint: #efefef;
    --white: #ffffff;
  }
  * { margin: 0; padding: 0; box-sizing: border-box; }
  html, body {
    width: 1200px; height: 1200px; overflow: hidden;
    background: var(--backdrop);
    font-family: "Montserrat", sans-serif;
  }
  .letterhead {
    position: absolute; left: 311px; top: 50px;
    width: 778px; height: 1100px;
    background: var(--paper);
    box-shadow: 0 6px 24px rgba(0,0,0,0.12);
  }
  .brand {
    position: absolute; top: 70px; left: 0; width: 100%;
    text-align: center;
  }
  .brand-mark {
    display: inline-flex; align-items: center; gap: 12px;
    font-size: 44px; font-weight: 400; letter-spacing: 2px;
    color: var(--taupe);
  }
  .brand-mark .square {
    width: 30px; height: 30px; background: var(--taupe);
  }
  .brand-tagline {
    margin-top: 6px;
    font-size: 13px; font-weight: 400; letter-spacing: 6px;
    color: var(--ink-grey);
  }
  .faint-emblem {
    position: absolute; left: 239px; top: 380px;
    width: 300px; height: 300px;
    background: var(--faint);
  }
  .contact-band {
    position: absolute; left: 0; bottom: 40px;
    width: 100%; height: 86px;
    background: var(--sand);
    display: flex; align-items: center; justify-content: space-between;
    padding: 0 40px;
    color: var(--white);
  }
  .contact-lines { font-size: 11px; line-height: 17px; font-weight: 400; }
  .contact-web { text-align: right; font-size: 11px; }
  .social { display: flex; gap: 6px; justify-content: flex-end; margin-bottom: 8px; }
  .social span { width: 14px; height: 14px; border-radius: 50%; background: var(--white); }
</style>
</head>
<body>
  <main class="letterhead">
    <header class="brand">
      <div class="brand-mark"><span class="square"></span>VERANTI</div>
      <div class="brand-tagline">MÓVEIS PLANEJADOS</div>
    </header>

    <div class="faint-emblem" role="img" aria-label="Marca da empresa em marca-d'água"></div>

    <footer class="contact-band">
      <div class="contact-lines">
        <p>Rua das Acácias, 120 - Sala 4</p>
        <p>01234-000 - São Paulo - SP</p>
        <p>Tel: 11 3456-7890</p>
        <p>Cel: 11 98765-4321</p>
      </div>
      <div class="contact-web">
        <div class="social"><span></span><span></span><span></span><span></span></div>
        <p>www.veranti.com.br</p>
      </div>
    </footer>
  </main>
</body>
</html>
```